Flyer für den Bereich Solarenergie
Zielgruppe
Guten Tag,
wir sind im Bereich Solarenergie tätig. Wir suchen nun Hallen mit großen Dächern, die wir anmieten können, um darauf Solaranlagen zu bauen. Wir machen dabei alles aus einer Hand. der Eigentümer muss nichts machen. Er bekommt sogar Geld von uns und das Dach ist sowieso meistens leer.
Aufgabenstellung
Wir möchten einen DINA4 Flyer den wir als PDF in Emails verschicken können. Farbdaten sollten Sie aus den Logodateien im Anhang entnehmen können. Richten Sie sich auch gerne an das Design des Logos und der Website. Dabei sollen kurz die wichtigsten Key Faktoren aufgelistet werden und das Unternehmen kurz dargestellt werden. Hier einmal die Texte:
Beschreibung zum Unternehmen:
Velumra ist Experte für grüne Energietechnik mit über 20 Jahren Erfahrung. Mit über 1.000 zufriedenen Kunden im Bereich Photovoltaikanlagen können wir auf einen großen Erfahrungsschatz zurückgreifen. Wenn wir am Werk sind, wird nicht nur das Klima geschont, sondern auch Sie als Kunde profitieren. Mit uns wird nachhaltiges Handeln kinderleicht und gleichzeitig rentabel.
Erwirtschaften auch Sie mit Ihrem Dach nun bares Geld!
Ihre Vorteile:
- Umwelt schonen durch das Produzieren von grünem Strom
- Dach schützen vor Emissionen
- Dachsanierungen anstatt von Mietzahlungen möglich
- Keine Kosten, da wir alle Kosten der Anträge, der Anlage und aller Arbeiten übernehmen
- Mieteinnahmen generieren!
Einzige Voraussetzung:
Dachfläche mit mind. 1.500qm
Worauf warten Sie?
Nehmen Sie jetzt Kontakt auf für eine entsprechende Machbarkeitsprüfung. Natürlich ist auch das Kostenlos.
velumra GmbH
Finkenstieg 87b
48159 Münster
T: +49 176 592 418 03
E: info@velumra-beispiel.de

```html
<!DOCTYPE html>
<html lang="de">
<head>
<meta charset="utf-8">
<title>velumra Energietechnik – Flyer</title>
<link href="https://fonts.googleapis.com/css2?family=Inter:wght@300;400;600;700&display=swap" rel="stylesheet">
<style>
  :root{
    --stage:#2c3140;
    --navy:#14223a;
    --navy-light:#3a5680;
    --lime:#b1ca12;
    --olive:#3f4a10;
    --ink:#3d3d3d;
    --text:#4a4a4a;
    --rule:#e6e6e6;
    --white:#ffffff;
  }
  *{box-sizing:border-box;margin:0;padding:0}
  html,body{width:1200px;height:1130px;overflow:hidden;background:var(--stage);font-family:'Inter',sans-serif}
  .flyer{position:absolute;left:280px;top:113px;width:640px;height:905px;background:var(--white);box-shadow:0 20px 50px rgba(0,0,0,.35);overflow:hidden}
  .hero{position:absolute;left:0;top:0;width:640px;height:214px;
    background:linear-gradient(180deg,#6d6a5c 0%,#3b5578 8%,#2c4466 35%,#1b2c48 70%,var(--navy) 100%)}
  .hero-photo{position:absolute;inset:0;background:linear-gradient(200deg,rgba(150,170,200,.35) 0%,rgba(20,34,58,0) 55%)}
  .brand{position:absolute;left:31px;top:30px;color:var(--white)}
  .brand-name{font-weight:300;font-size:30px;letter-spacing:.5px;line-height:1}
  .brand-tag{font-size:6.5px;letter-spacing:4px;margin-top:6px}
  .hero-title{position:absolute;left:31px;top:106px;color:var(--white);font-weight:700;font-size:29.5px;letter-spacing:-.2px}
  .hero-sub{position:absolute;left:31px;top:144px;color:var(--lime);font-weight:300;font-size:19px}
  .accent-bar{position:absolute;left:0;top:206px;width:380px;height:8px;background:var(--lime)}
  .intro{position:absolute;left:0;top:214px;width:380px;height:302px;background:linear-gradient(180deg,#fff 77%,#fafafa 77%)}
  .intro h2{position:absolute;left:31px;top:44px;width:320px;font-size:18px;line-height:21px;font-weight:700;color:var(--ink)}
  .intro p{position:absolute;left:31px;width:320px;font-size:12.6px;line-height:19px;color:var(--text)}
  .intro .p1{top:108px}
  .intro .p2{top:222px}
  .roof-photo{position:absolute;left:380px;top:214px;width:260px;height:302px;
    background:linear-gradient(180deg,#e3e6ea 0%,#cfd6de 38%,#6b7a6a 46%,#4a5f92 60%,#2f4a8a 80%,#283a66 100%)}
  .benefits{position:absolute;left:0;top:516px;width:380px;list-style:none;border-top:1px solid var(--rule)}
  .benefit{height:78px;border-bottom:1px solid var(--rule);display:flex;align-items:center;padding-left:31px}
  .benefit:last-child{border-bottom:none}
  .benefit svg{width:26px;height:26px;flex:none}
  .benefit span{margin-left:24px;font-size:11.4px;line-height:14.5px;color:var(--text);width:275px}
  .cta{position:absolute;left:380px;top:516px;width:260px;height:389px;background:var(--lime);color:var(--white)}
  .cta .req{position:absolute;left:25px;top:36px;font-size:17.5px;line-height:21px;font-weight:700;color:var(--olive)}
  .cta hr{position:absolute;left:27px;top:98px;width:209px;border:none;border-top:1.5px solid var(--white)}
  .cta h3{position:absolute;left:25px;top:120px;font-size:17.5px;line-height:21px;font-weight:700}
  .cta p{position:absolute;left:25px;top:178px;width:225px;font-size:11.5px;line-height:17px}
  .contact{position:absolute;left:25px;top:272px;font-size:12.4px;line-height:17px}
  .contact-line{display:flex;align-items:center;margin-top:8px}
  .contact-line svg{width:13px;height:13px;margin-right:9px}
</style>
</head>
<body>
<div class="flyer">
  <header class="hero">
    <div class="hero-photo" role="img" aria-label="Weites Feld aus Solarmodulen unter Abendhimmel"></div>
    <div class="brand">
      <div class="brand-name">velumra</div>
      <div class="brand-tag">ENERGIETECHNIK</div>
    </div>
    <h1 class="hero-title">Ihr Experte für grüne Energietechnik</h1>
    <div class="hero-sub">Seit über 20 Jahren</div>
  </header>
  <div class="accent-bar"></div>

  <section class="intro">
    <h2>Erwirtschaften auch Sie mit Ihrem Dach bares Geld!</h2>
    <p class="p1">Mit über 1.000 zufriedenen Kunden im Bereich Photovoltaikanlagen können wir auf einen großen Erfahrungsschatz zurückgreifen. Wenn wir am Werk sind, wird nicht nur das Klima geschont, sondern auch Sie als Kunde profitieren.</p>
    <p class="p2">Mit uns wird nachhaltiges Handeln kinderleicht und gleichzeitig rentabel.</p>
  </section>
  <div class="roof-photo" role="img" aria-label="Solarmodule auf einem Flachdach mit Stadtsilhouette im Hintergrund"></div>

  <ul class="benefits">
    <li class="benefit">
      <svg viewBox="0 0 24 24"><path d="M12 1 3 4v7c0 6 4 10 9 12 5-2 9-6 9-12V4z" fill="#b1ca12"/><path d="m7.5 12 3 3 6-6" fill="none" stroke="#fff" stroke-width="2.2" stroke-linecap="round" stroke-linejoin="round"/></svg>
      <span>Dach schützen vor Emissionen</span>
    </li>
    <li class="benefit">
      <svg viewBox="0 0 24 24"><circle cx="12" cy="12" r="11" fill="#b1ca12"/><text x="12" y="16.5" text-anchor="middle" font-family="Inter,sans-serif" font-size="13" font-weight="700" fill="#fff">€</text></svg>
      <span>Mieteinnahmen generieren</span>
    </li>
    <li class="benefit">
      <svg viewBox="0 0 24 24"><path d="M9 1h8l4 4v13h-3V5.5L14.5 2H9z" fill="#b1ca12"/><path d="M4 5h9l4 4v14H4z" fill="#b1ca12"/><path d="M7.5 15h5M7.5 18h5" stroke="#fff" stroke-width="1.6"/></svg>
      <span>Keine Kosten, da wir alle Kosten der Anträge, der Anlage und aller Arbeiten übernehmen.</span>
    </li>
    <li class="benefit">
      <svg viewBox="0 0 24 24"><path d="M15 1 5 13h6l-3 10 11-13h-6z" fill="#b1ca12"/></svg>
      <span>Umwelt schonen durch das Produzieren von grünem Strom</span>
    </li>
    <li class="benefit">
      <svg viewBox="0 0 24 24"><rect x="2" y="2" width="8" height="8" rx="1.5" fill="#b1ca12"/><rect x="14" y="14" width="8" height="8" rx="1.5" fill="#b1ca12"/><path d="M20 10V6h-6m2-2-2 2 2 2M4 14v4h6m-2-2 2 2-2 2" fill="none" stroke="#b1ca12" stroke-width="1.8" stroke-linecap="round" stroke-linejoin="round"/></svg>
      <span>Dachsanierungen anstatt von Mietzahlungen möglich</span>
    </li>
  </ul>

  <aside class="cta">
    <div class="req">Schon ab einer<br>Dachfläche von 1500qm</div>
    <hr>
    <h3>Worauf warten<br>Sie noch?</h3>
    <p>Nehmen Sie jetzt Kontakt auf für eine entsprechende Machbarkeitsprüfung. Natürlich ist auch das kostenlos.</p>
    <address class="contact" style="font-style:normal">
      <div>velumra GmbH</div>
      <div>Finkenstieg 87b, 48159 Münster</div>
      <div class="contact-line" style="margin-top:18px">
        <svg viewBox="0 0 24 24"><path d="M6.6 10.8a15 15 0 0 0 6.6 6.6l2.2-2.2c.3-.3.7-.4 1-.2 1.1.4 2.3.6 3.6.6.6 0 1 .4 1 1V20c0 .6-.4 1-1 1A17 17 0 0 1 3 4c0-.6.4-1 1-1h3.5c.6 0 1 .4 1 1 0 1.3.2 2.5.6 3.6.1.3 0 .7-.2 1z" fill="#fff"/></svg>
        +49 176 592 418 03
      </div>
      <div class="contact-line">
        <svg viewBox="0 0 24 24"><rect x="2" y="4" width="20" height="16" rx="2" fill="#fff"/><path d="m3 6 9 7 9-7" fill="none" stroke="#b1ca12" stroke-width="2"/></svg>
        info@velumra-beispiel.de
      </div>
    </address>
  </aside>
</div>
</body>
</html>
```